Create a memorable Web Design for real estate branding

we are a Minnepolis brokerage and boutique housing specialist with over 27 years of experience in the Global furnished housing industry, servicing the Greater Los Angeles area. Specializing in “warm environments” we offer a customized approach to satisfying our guests and client’s needs by offering a wide array of options in highly desirable areas. Additionally, Lanterly Homes Collective offers assistance and expertise to home buyers, sellers and investors.

Industry/Entity Type

Real Estate

Number of Pages Required

1 page

Font styles to use
Serif
Sans Serif
Decorative

```html
<!DOCTYPE html>
<html lang="en">
<head>
<meta charset="utf-8">
<title>Halvard Reed Real Estate</title>
<link href="https://fonts.googleapis.com/css2?family=Cinzel:wght@400;700&family=Great+Vibes&family=Mulish:wght@400;600;700&display=swap" rel="stylesheet">
<style>
:root{
  --teal:#11a891;
  --teal-dark:#0b8f7b;
  --lime:#9bc73b;
  --ink:#222;
  --text:#5a5a5a;
  --footer:#dddddd;
  --white:#fff;
  --sans:'Mulish',Arial,sans-serif;
  --serif:'Cinzel',Georgia,serif;
  --script:'Great Vibes',cursive;
}
*{box-sizing:border-box;margin:0;padding:0}
html,body{width:1200px;height:2236px;overflow:hidden}
body{font-family:var(--sans);color:var(--text);background:var(--white);position:relative}
.abs{position:absolute}

/* header */
.site-header{position:absolute;left:0;top:0;width:1200px;height:109px;background:var(--white)}
.brand{position:absolute;left:75px;top:22px;font-family:var(--sans);font-weight:700;font-size:38px;line-height:44px;color:var(--teal)}
.brand-sub{position:absolute;left:190px;top:62px;font-family:var(--sans);font-weight:700;font-size:22px;color:var(--teal);letter-spacing:2px}
.top-contact{position:absolute;right:75px;top:16px;font-size:13px;color:#555}
.top-contact b{color:var(--teal);font-weight:400}
.top-contact span{margin-left:24px}
.main-nav{position:absolute;right:75px;top:76px;display:flex;gap:32px;font-size:14px;color:#444}
.main-nav .active{color:var(--teal)}

/* hero */
.hero{position:absolute;left:0;top:109px;width:1200px;height:553px;
  background:linear-gradient(180deg,#e9eaec 0%,#dfe1e2 55%,#bfc2c4 80%,#6f7273 100%)}
.hero-copy{position:absolute;left:387px;top:32px;width:430px}
.hero-city{font-size:19px;letter-spacing:1px;color:#222}
.hero-script{font-family:var(--script);font-size:50px;line-height:50px;color:#111}
.hero-tag{text-align:right;font-size:20px;color:#222;margin-top:2px}
.hero-tag b{color:var(--teal);font-weight:400}

/* welcome */
.welcome{position:absolute;left:0;top:662px;width:1200px;height:386px}
.welcome h1{position:absolute;left:75px;top:42px;font-family:var(--serif);font-weight:400;font-size:24px;color:#222;font-variant:small-caps}
.welcome p{position:absolute;left:75px;top:92px;width:690px;font-size:13.4px;line-height:24.2px;color:#555}
.quick-contact{position:absolute;left:793px;top:0;width:332px;height:386px;background:var(--teal);padding:20px 23px}
.quick-contact h2{font-family:var(--serif);font-weight:400;font-size:25px;color:var(--white);font-variant:small-caps;margin-bottom:22px}
.field{display:block;width:286px;height:34px;background:var(--white);border-radius:3px;margin-bottom:11px;font-size:12px;color:#888;padding:9px 9px}
.field.message{height:98px}
.submit{width:286px;height:43px;background:var(--lime);border-radius:3px;color:var(--white);font-weight:700;font-size:18px;text-align:center;line-height:43px;margin-top:7px}

/* services */
.services{position:absolute;left:0;top:1048px;width:1200px;height:439px;background:linear-gradient(180deg,#f4f4f4,#eeeeee)}
.services-kicker{position:absolute;left:0;top:42px;width:1200px;text-align:center;font-family:var(--serif);font-size:18px;color:#222;font-variant:small-caps}
.services-title{position:absolute;left:0;top:64px;width:1200px;text-align:center;font-family:var(--serif);font-size:22px;color:#222;letter-spacing:1px}
.service{position:absolute;top:134px;width:330px;text-align:center}
.service-icon{width:118px;height:118px;border-radius:50%;background:var(--white);margin:0 auto;box-shadow:12px 12px 18px rgba(0,0,0,.12);display:flex;align-items:center;justify-content:center}
.service h3{font-weight:600;font-size:19px;color:#222;margin-top:40px}
.service p{font-size:13.4px;line-height:22px;color:#555;margin-top:20px;padding:0 8px}

/* testimonials */
.testimonials{position:absolute;left:0;top:1487px;width:1200px;height:340px}
.testimonials-bg{position:absolute;inset:0;background:linear-gradient(90deg,#1a9f7e 0%,#14b59c 40%,#12a996 70%,#0d8c7c 100%)}
.testimonials h2{position:absolute;left:0;top:36px;width:1200px;text-align:center;font-family:var(--serif);font-weight:400;font-size:24px;color:var(--white);font-variant:small-caps}
.review{position:absolute;top:137px;width:331px;height:155px;background:var(--white);padding:52px 18px 0}
.avatar{position:absolute;left:18px;top:-27px;width:62px;height:62px;background:linear-gradient(160deg,#c9b7a8,#8f8074);border:2px solid var(--white)}
.review-name{position:absolute;left:100px;top:10px;font-size:15px;line-height:20px;color:#111;font-weight:600}
.review p{font-size:13px;line-height:20px;color:#555;margin-top:0}

/* info band */
.info-band{position:absolute;left:0;top:1827px;width:1200px;height:119px;background:var(--lime)}
.info{position:absolute;top:26px;padding-left:36px;font-size:13.4px;line-height:20px;color:#111}
.info svg{position:absolute;left:0;top:2px}
.info b{font-weight:700;font-size:15px;display:block}

/* footer */
.site-footer{position:absolute;left:0;top:1946px;width:1200px;height:290px;background:var(--footer)}
.foot-col{position:absolute;top:32px;font-size:13.4px;line-height:26px;color:#555}
.foot-col h4{font-weight:600;font-size:15px;color:#111;margin-bottom:4px;line-height:22px}
.newsletter{position:absolute;left:614px;top:32px}
.newsletter h4{font-weight:600;font-size:15px;color:#111}
.nl-field{position:absolute;top:38px;width:243px;height:39px;background:var(--white);font-size:12px;color:#666;padding:12px 10px}
.nl-btn{position:absolute;left:0;top:95px;width:93px;height:39px;background:var(--teal);color:var(--white);font-size:13px;text-align:center;line-height:39px}
.footer-bar{position:absolute;left:0;top:230px;width:1200px;height:60px;border-top:1px solid #cfcfcf}
.copyright{position:absolute;left:73px;top:19px;font-size:13px;color:#555}
.social{position:absolute;right:75px;top:12px;display:flex;gap:7px}
.social span{width:30px;height:30px;border:2px solid #b5b5b5;border-radius:50%}
</style>
</head>
<body>

<header class="site-header">
  <div class="brand">Halvard Reed</div>
  <div class="brand-sub">REAL ESTATE</div>
  <div class="top-contact"><b>T:</b> 1800 555 0142<span><b>E:</b> info@halvardreedhomes.com</span></div>
  <nav class="main-nav">
    <span class="active">HOME</span><span>ABOUT US</span><span>OUR CLIENTS</span><span>PROPERTIES</span><span>TESTIMONIALS</span><span>CONTACT US</span>
  </nav>
</header>

<section class="hero" role="img" aria-label="Bright living room with a white sofa, colourful cushions, a light blue armchair and a striped rug">
  <div class="hero-copy">
    <div class="hero-city">MINNEPOLIS</div>
    <div class="hero-script">Brokerage and Boutique</div>
    <div class="hero-tag"><b>HOUSING</b> SPECIALIST</div>
  </div>
</section>

<section class="welcome">
  <h1>Welcome to Halvard Reed Real Estate</h1>
  <p>Lorem ipsum dolor sit amet, consectetuer adipiscing elit, sed diam nonummy nibh euismod tincidunt ut laoreet dolore magna aliquam erat volutpat. Ut wisi enim ad minim veniam, quis nostrud exerci tation ullamcorper suscipit lobortis nisl ut aliquip ex ea commodo consequat. Duis autem vel eum iriure dolor in hendrerit in vulputate velit esse molestie consequat, vel illum dolore eu feugiat nulla facilisis at vero eros et accumsan et iusto odio dignissim qui blandit praesent luptatum zzril delenit augue duis dolore te feugait nulla facilisi. Nam liber tempor cum soluta nobis eleifend option congue nihil imperdiet doming id quod mazim placerat facer possim assum. Typi non habent claritatem insitam; est usus legentis in iis qui facit eorum claritatem. Investigationes demonstraverunt lectores legere me lius quod ii legunt saepius.</p>
  <aside class="quick-contact">
    <h2>Quick Contact</h2>
    <span class="field">Name</span>
    <span class="field">Email Address</span>
    <span class="field">Phone Number</span>
    <span class="field message">Message</span>
    <div class="submit">SUBMIT</div>
  </aside>
</section>

<section class="services">
  <div class="services-kicker">Lanterly Homes Collective</div>
  <div class="services-title">OFFERS ASSISTANCE AND EXPERTISE</div>

  <div class="service" style="left:75px">
    <div class="service-icon">
      <svg width="56" height="56" viewBox="0 0 56 56" fill="none" stroke="#8cc23c" stroke-width="3"><path d="M14 26 L30 12 L46 26 V40 H14 Z"/><path d="M4 44 H20 L34 50 L52 42"/><text x="30" y="35" font-size="14" text-anchor="middle" fill="#8cc23c" stroke="none" font-family="Arial,sans-serif" font-weight="700">$</text></svg>
    </div>
    <h3>HOME BUYERS</h3>
    <p>Ut wisi enim ad minim veniam, quis nostrud exerci tation ullamcorper suscipit lobortis nisl ut aliquip ex ea commodo consequat.</p>
  </div>

  <div class="service" style="left:435px">
    <div class="service-icon">
      <svg width="56" height="56" viewBox="0 0 56 56"><path d="M22 24 L38 10 L54 24 V42 H22 Z" fill="#8cc23c"/><circle cx="16" cy="36" r="12" fill="#8cc23c"/><rect x="34" y="30" width="8" height="12" fill="#fff"/></svg>
    </div>
    <h3>SELLERS</h3>
    <p>Ut wisi enim ad minim veniam, quis nostrud exerci tation ullamcorper suscipit lobortis nisl ut aliquip ex ea commodo consequat.</p>
  </div>

  <div class="service" style="left:795px">
    <div class="service-icon">
      <svg width="56" height="56" viewBox="0 0 56 56"><circle cx="28" cy="20" r="14" fill="#8cc23c"/><text x="28" y="26" font-size="16" text-anchor="middle" fill="#fff" font-family="Arial,sans-serif" font-weight="700">$</text><path d="M6 52 Q6 38 18 38 H38 Q50 38 50 52 Z" fill="#8cc23c"/></svg>
    </div>
    <h3>INVESTORS</h3>
    <p>Ut wisi enim ad minim veniam, quis nostrud exerci tation ullamcorper suscipit lobortis nisl ut aliquip ex ea commodo consequat.</p>
  </div>
</section>

<section class="testimonials">
  <div class="testimonials-bg" role="img" aria-label="Teal-tinted photo of a smiling man with glasses working at a desk"></div>
  <h2>Happy Clients</h2>

  <article class="review" style="left:75px">
    <div class="avatar" role="img" aria-label="Client portrait"></div>
    <div class="review-name">Daniel Ostrow,<br>Lorem ipsum dolor sit</div>
    <p>Lorem ipsum dolor sit amet, consectetuer adipiscing elit, sed diam nonummy nibh euismod tincidunt ut laoreet dolore magna aliquam erat volutpat. "</p>
  </article>
  <article class="review" style="left:434px">
    <div class="avatar" role="img" aria-label="Client portrait"></div>
    <div class="review-name">Peter Lindqvist,<br>Lorem ipsum dolor sit</div>
    <p>Lorem ipsum dolor sit amet, consectetuer adipiscing elit, sed diam nonummy nibh euismod tincidunt ut laoreet dolore magna aliquam erat volutpat. "</p>
  </article>
  <article class="review" style="left:794px">
    <div class="avatar" role="img" aria-label="Client portrait"></div>
    <div class="review-name">Owen Carraway,<br>Lorem ipsum dolor sit</div>
    <p>Lorem ipsum dolor sit amet, consectetuer adipiscing elit, sed diam nonummy nibh euismod tincidunt ut laoreet dolore magna aliquam erat volutpat. "</p>
  </article>
</section>

<section class="info-band">
  <div class="info" style="left:73px">
    <svg width="18" height="24" viewBox="0 0 18 24" fill="none" stroke="#222" stroke-width="1.6"><path d="M9 23 C9 23 2 14 2 9 A7 7 0 0 1 16 9 C16 14 9 23 9 23 Z"/><circle cx="9" cy="9" r="2.5"/></svg>
    <b>Halvard Reed Real Estate</b>228, Lorem ipsum dolor sit,<br>dosis amnet - 858595
  </div>
  <div class="info" style="left:433px">
    <svg width="16" height="26" viewBox="0 0 16 26" fill="none" stroke="#222" stroke-width="1.6"><rect x="1.5" y="1" width="13" height="24" rx="2"/><line x1="1.5" y1="20" x2="14.5" y2="20"/></svg>
    <b>Broker Referrals</b>T: 1800 555 0141<br>T: 1800 555 0142
  </div>
  <div class="info" style="left:793px">
    <svg width="28" height="20" viewBox="0 0 28 20" fill="none" stroke="#222" stroke-width="1.6"><rect x="6" y="2" width="20" height="15"/><path d="M6 2 L16 11 L26 2"/><line x1="0" y1="8" x2="4" y2="8"/><line x1="1" y1="12" x2="4" y2="12"/></svg>
    <b>Email Information</b>offices@halvardreedhomes.com<br>info@halvardreedhomes.com
  </div>
</section>

<footer class="site-footer">
  <div class="foot-col" style="left:73px">
    <h4>Quick Links</h4>Home<br>About Us<br>Our Clients<br>Properties<br>Testimonials<br>Contact Us
  </div>
  <div class="foot-col" style="left:297px">
    <h4>Information</h4>About Us<br>Contact Us<br>Testimonials<br>FAQs
  </div>
  <div class="foot-col" style="left:474px">
    <h4>&nbsp;</h4>Terms of Use<br>Privacy Policy<br>Specials<br>Sitemap
  </div>
  <div class="newsletter">
    <h4>Subscribe Our Newsletter Today!!!</h4>
    <span class="nl-field" style="left:0">Name</span>
    <span class="nl-field" style="left:252px">Email Address</span>
    <div class="nl-btn">SUBSCRIBE</div>
  </div>
  <div class="footer-bar">
    <div class="copyright">Copyright ©2016 Halvard Reed Real Estate. All Rights Reserved</div>
    <div class="social" aria-label="Social links"><span></span><span></span><span></span><span></span><span></span></div>
  </div>
</footer>

</body>
</html>
```